Business Card Design For Financial Company

Create a new design for company's business card. The corporate logo is attached in several formats. Our new website design is also attached and we would like the business cards to reflect this.
Card needs to contain the following info:
Name
Job Title
Legal company name - eg Volmar Capital (Asia) Ltd
Address - eg 612-15 Dorrance Plaza,47 Faverly Street, Hong Kong
Direct tel
Main tel
Fax
Email
Website URL
MS word format preferred. Other formats that can be edited on standard PC also OK.
Please note the the "VOLMAR" logo nameĀ font is "Gill Sans MT" on Windows
Target Market(s)
Instituation Investors
Industry/Entity Type
Business

```html
<!DOCTYPE html>
<html lang="en">
<head>
<meta charset="utf-8">
<title>Volmar Capital – Business Card</title>
<link href="https://fonts.googleapis.com/css2?family=Arimo:wght@400;700&display=swap" rel="stylesheet">
<style>
  :root {
    --stage-dark: #1b1b1b;
    --stage-light: #5a5a5a;
    --brand-red: #d0202a;
    --brand-red-deep: #b3141d;
    --ink: #111111;
    --paper: #ffffff;
    --rule: #1a1a1a;
    --fade-grey: #b8b8b8;
  }
  * { box-sizing: border-box; margin: 0; padding: 0; }
  html, body { width: 1200px; height: 877px; overflow: hidden; }
  body {
    background: radial-gradient(ellipse at 50% 35%, var(--stage-light) 0%, var(--stage-dark) 75%);
    font-family: "Arimo", Arial, sans-serif;
    position: relative;
  }
  .card {
    position: absolute;
    top: 284px;
    width: 540px;
    height: 309px;
    overflow: hidden;
    box-shadow: 0 14px 30px rgba(0,0,0,0.55);
  }
  .card--front { left: 40px; background: var(--brand-red); }
  .card--back { left: 620px; background: var(--paper); color: var(--ink); }

  .tagline {
    position: absolute;
    left: 48px;
    top: 64px;
    color: var(--paper);
    font-weight: 700;
    font-size: 29px;
    line-height: 25px;
    letter-spacing: 0.2px;
  }
  .front-rule {
    position: absolute;
    left: 0;
    top: 232px;
    width: 400px;
    height: 3px;
    background: var(--rule);
  }

  .brand {
    position: absolute;
    right: 26px;
    bottom: 26px;
    display: flex;
    align-items: center;
    gap: 10px;
  }
  .brand__dot {
    width: 34px;
    height: 34px;
    border-radius: 50%;
    background: var(--brand-red-deep);
  }
  .card--front .brand__dot { background: var(--paper); }
  .brand__name {
    font-weight: 700;
    font-size: 24px;
    letter-spacing: 1px;
    color: var(--brand-red-deep);
  }
  .card--front .brand__name { color: var(--paper); }

  .contact { position: absolute; left: 34px; top: 34px; }
  .contact__name { font-size: 23px; font-weight: 400; }
  .contact__title { font-size: 10.5px; margin-top: 3px; }
  .contact__company { font-size: 13.5px; font-weight: 700; margin-top: 18px; }
  .contact__address { font-size: 13.5px; line-height: 16px; margin-top: 2px; }
  .contact__lines { margin-top: 22px; font-size: 13.5px; line-height: 16px; }
  .contact__lines b { font-weight: 700; }
  .contact__email { margin-top: 6px; }
  .contact__web { font-size: 15.5px; font-weight: 700; margin-top: 12px; }

  .back-fade {
    position: absolute;
    left: 0;
    bottom: 0;
    width: 100%;
    height: 38px;
    background: linear-gradient(to bottom, var(--paper), var(--fade-grey));
  }
</style>
</head>
<body>
  <section class="card card--front" aria-label="Card front">
    <h1 class="tagline">Independant<br>Research<br>Marketing<br>and<br>Execution</h1>
    <div class="front-rule"></div>
    <div class="brand">
      <span class="brand__dot"></span>
      <span class="brand__name">VOLMAR</span>
    </div>
  </section>

  <section class="card card--back" aria-label="Card back">
    <div class="contact">
      <p class="contact__name">Daniel Harlow</p>
      <p class="contact__title">Managing Director</p>
      <p class="contact__company">Volmar Capital (Asia) Ltd</p>
      <p class="contact__address">612-15 Dorrance Plaza,<br>47 Faverly Street, Hong Kong</p>
      <div class="contact__lines">
        <p><b>M.</b> 0492 538 207</p>
        <p><b>P.</b> (02) 3816 4590</p>
        <p><b>F.</b> (02) 3816 4591</p>
        <p class="contact__email"><b>E.</b> dharlow@volmarcapital.com</p>
      </div>
      <p class="contact__web">www.volmarcapital.com</p>
    </div>
    <div class="back-fade"></div>
    <div class="brand">
      <span class="brand__dot"></span>
      <span class="brand__name">VOLMAR</span>
    </div>
  </section>
</body>
</html>
```